依頼概要
■依頼の目的/概要
弊社が販売しているフルーツトマト(高糖度トマト)のパッケージのラベルデザインをお願いします。

■依頼詳細
弊社はトマトの栽培をしています。場所は長崎県壱岐市で玄界灘の島です。
ソラリム栽培というフィルムで栽培する新しい栽培方法です。島内のスーパーで販売しており大変好評です。糖度が8度以上あり、小さな子供さんからお年寄りまで喜んで食べて頂いています。トマト嫌いの人もこのトマトなら食べれるといって食べる方もいらっしゃいます。予想以上の好評で今回栽培面積を増やし関東への販路を考えております。これまで「ほしうらら」(子供が美味しくてパクパク食べてすぐ無くなり、また買ってと何回もせがまれママを泣かせる)というネーミングで販売していましたが。関東進出を期にネーミングを「紅澄野」又は「べに澄野」にバージョンアップして、新しいラベルの作成を企画しております。
<ラベルの仕様>
1.トマト1粒が20g~40gのミディートマトを150g~250gのパッケージで販売することを想定して、そのパッケージに貼るラベルです。
2.ラベルの大きさは、36×45角丸5R (mm)
3.ラベルに盛込む内容は添付ファイルの内容と同じで「ほしうらら」を「紅澄野」又は「べに澄野」に変更(デザインにマッチする方を選択して下さい)

■その他要望
高品質が売りですから、高級感と「一目で食べてみたい」と思うようなラベルにして欲しい。ネーミングは変更しない方がいいという方は「ほしうらら」のままでも構いません。
■ 選んだ理由

1.産地壱岐が強調されたデザインである。
2.表現したい項目が全て網羅されている。
3.デザインがシンプルでわかり易い。

■ 提案者全員のお礼・コメント

ラベルデザインの依頼は初めてでしたが、沢山のご提案を
頂き感謝しております。
多くの方のご提案有難うございました。

```html
<!DOCTYPE html>
<html lang="ja">
<head>
<meta charset="utf-8">
<title>べに澄野 ラベル</title>
<link rel="stylesheet" href="https://fonts.googleapis.com/css2?family=Yuji+Syuku&family=Noto+Serif+JP:wght@700&display=swap">
<style>
  :root {
    --paper: #ffffff;
    --tomato-red: #c8141d;
    --tomato-deep: #b30f19;
    --tomato-soft: #c4303a;
    --navy: #1f2a4a;
    --navy-soft: #e4e7ef;
    --gold: #b08d4a;
    --ink-light: #ffffff;
    --ink-dark: #1f2a4a;
  }
  html, body {
    margin: 0;
    padding: 0;
    width: 867px;
    height: 1200px;
    overflow: hidden;
    background: var(--paper);
  }
  .sheet {
    position: relative;
    width: 867px;
    height: 1200px;
  }
  .label {
    position: absolute;
    left: 236px;
    width: 400px;
    height: 316px;
    border-radius: 40px;
    box-sizing: border-box;
  }
  .label--red { top: 200px; background: var(--tomato-red); color: var(--ink-light); }
  .label--navy { top: 680px; background: var(--navy); color: var(--ink-dark); }
  .label-field {
    position: absolute;
    inset: 10px;
    border-radius: 32px;
  }
  .label--red .label-field { background: var(--tomato-deep); }
  .label--navy .label-field { inset: 16px 16px 14px 16px; border-radius: 28px; background: var(--paper); }
  .ridge-art {
    position: absolute;
    left: 24px;
    top: 24px;
    width: 352px;
    height: 78px;
    border-radius: 12px;
  }
  .label--red .ridge-art { background: linear-gradient(180deg, var(--tomato-soft), var(--tomato-deep)); }
  .label--navy .ridge-art { background: linear-gradient(180deg, var(--navy-soft), var(--paper)); }
  .brand-name {
    position: absolute;
    left: 98px;
    top: 112px;
    margin: 0;
    font-family: "Yuji Syuku", "Noto Serif JP", serif;
    font-weight: 400;
    font-size: 70px;
    line-height: 76px;
  }
  .brand-name span { display: block; }
  .brand-name span + span { padding-left: 48px; }
  .origin {
    position: absolute;
    right: 56px;
    top: 124px;
    margin: 0;
    writing-mode: vertical-rl;
    font-family: "Yuji Syuku", "Noto Serif JP", serif;
    font-size: 17px;
    letter-spacing: 2px;
  }
  .sugar-badge {
    position: absolute;
    left: 30px;
    top: 150px;
    width: 44px;
    height: 132px;
    margin: 0;
    background: var(--gold);
    color: var(--ink-light);
    writing-mode: vertical-rl;
    font-family: "Noto Serif JP", serif;
    font-weight: 700;
    font-size: 19px;
    line-height: 44px;
    text-align: center;
  }
  .sugar-badge .num { text-combine-upright: all; }
</style>
</head>
<body>
<main class="sheet">

  <section class="label label--red" aria-label="べに澄野 赤ラベル">
    <div class="label-field"></div>
    <div class="ridge-art" role="img" aria-label="山の稜線の線画"></div>
    <h1 class="brand-name"><span>べに</span><span>澄野</span></h1>
    <p class="origin">長崎県産</p>
    <p class="sugar-badge">糖度<span class="num">8</span>以上</p>
  </section>

  <section class="label label--navy" aria-label="べに澄野 紺ラベル">
    <div class="label-field"></div>
    <div class="ridge-art" role="img" aria-label="山の稜線の線画"></div>
    <h2 class="brand-name"><span>べに</span><span>澄野</span></h2>
    <p class="origin">長崎県産</p>
    <p class="sugar-badge">糖度<span class="num">8</span>以上</p>
  </section>

</main>
</body>
</html>
```